Velkaros Pendants

Brightmoor Studio is a growing wedding ring wholesaler/manufacturer based in NYC. We have recently teamed up with a cross designer from Greece and added their line of cross pendants to our product line. We would like to introduce the product to our customers. We are looking for a clean looking postcard. Is it possible to remove the style number and weights from the bottom right corner of each image?
We will provide wording, etc. upon request.

Thanks.
Updates

We would like all or most images to be on the postcard, front and back is fine. Thanks!!

Industry/Entity Type

Wedding

```html
<!DOCTYPE html>
<html lang="en">
<head>
<meta charset="utf-8">
<title>Handmade Designer Crosses – Brightmoor Studio</title>
<link rel="stylesheet" href="https://fonts.googleapis.com/css2?family=Dancing+Script:wght@500;600&family=Raleway:wght@300&family=Cinzel:wght@500&display=swap">
<style>
  :root {
    --page-bg: #ffffff;
    --card-center: #f4f4f4;
    --card-edge: #c9c9c9;
    --ink: #2b2b2b;
    --subtitle: #9a9a9a;
    --tile-dark: #333333;
    --tile-text: #ffffff;
    --photo-light: #ffffff;
    --photo-mid: #e6e6e6;
  }
  * { margin: 0; padding: 0; box-sizing: border-box; }
  html, body {
    width: 1200px;
    height: 1000px;
    overflow: hidden;
    background: var(--page-bg);
  }
  .postcard {
    position: absolute;
    left: 279px;
    top: 83px;
    width: 643px;
    height: 835px;
    background: radial-gradient(ellipse at 50% 40%, var(--card-center) 0%, #e4e4e4 55%, var(--card-edge) 100%);
  }
  .headline {
    position: absolute;
    left: 0;
    right: 0;
    top: 22px;
    text-align: center;
    font-family: "Dancing Script", cursive;
    font-weight: 500;
    color: var(--ink);
    line-height: 1;
  }
  .headline .line-one { display: block; font-size: 56px; }
  .headline .line-two { display: block; font-size: 60px; margin-top: -4px; }
  .studio-name {
    position: absolute;
    left: 0;
    right: 0;
    top: 136px;
    text-align: center;
    font-family: "Raleway", sans-serif;
    font-weight: 300;
    font-size: 32px;
    letter-spacing: 15px;
    color: var(--subtitle);
    text-transform: lowercase;
    white-space: nowrap;
  }
  .feature-grid {
    position: absolute;
    left: 77px;
    top: 226px;
    display: grid;
    grid-template-columns: repeat(3, 155px);
    grid-auto-rows: 126px;
    column-gap: 13px;
    row-gap: 9px;
  }
  .tile-photo {
    background: radial-gradient(circle at 50% 50%, var(--photo-mid) 0%, var(--photo-light) 45%);
  }
  .tile-word {
    background: var(--tile-dark);
    color: var(--tile-text);
    display: flex;
    align-items: center;
    justify-content: center;
    text-align: center;
    font-family: "Dancing Script", cursive;
    font-weight: 600;
    font-size: 30px;
    line-height: 1.05;
  }
  .tagline {
    position: absolute;
    left: 0;
    right: 0;
    top: 764px;
    text-align: center;
    font-family: "Cinzel", serif;
    font-weight: 500;
    font-size: 15px;
    letter-spacing: 1px;
    color: var(--ink);
  }
</style>
</head>
<body>
  <main class="postcard">
    <h1 class="headline">
      <span class="line-one">Handmade</span>
      <span class="line-two">Designer Crosses</span>
    </h1>
    <p class="studio-name">brightmoor studio</p>

    <section class="feature-grid">
      <div class="tile-photo" role="img" aria-label="Silver cross pendant with open centre"></div>
      <div class="tile-word">Hand Made</div>
      <div class="tile-photo" role="img" aria-label="Silver cross pendant with curved arms"></div>

      <div class="tile-word">Designer</div>
      <div class="tile-photo" role="img" aria-label="Silver cross pendant set with stones"></div>
      <div class="tile-word">Custom<br>Design</div>

      <div class="tile-photo" role="img" aria-label="Silver open outline cross pendant"></div>
      <div class="tile-word">Quality<br>Work</div>
      <div class="tile-photo" role="img" aria-label="Silver layered cross pendant"></div>

      <div class="tile-word">Special</div>
      <div class="tile-photo" role="img" aria-label="Silver stepped cross pendant"></div>
      <div class="tile-word">Elegant</div>
    </section>

    <p class="tagline">QUALITY WORK FOR YOUR PRICELESS POSESSIONS</p>
  </main>
</body>
</html>
```